New Business Card

Use website for color, logo and theme.

http://www.plumwickonline.com/

Back side of card should be programs listed on home page of website

1) Phone Number is (800) 555-0142 x23
2) Fax (240) 555-0187
3) Address is - 647 W Harlowe Street, Suite 312, Baltimore, MD 21201
4) NMLS #738516

```html
<!DOCTYPE html>
<html lang="en">
<head>
<meta charset="utf-8">
<title>Plumwick Financial Services – Business Card</title>
<link href="https://fonts.googleapis.com/css2?family=Arimo:wght@400;700&display=swap" rel="stylesheet">
<style>
  :root {
    --page-bg: #e9eaec;
    --brand-blue: #0d5aa7;
    --brand-blue-dark: #0a4a8c;
    --brand-gold: #a8913f;
    --ink: #2a2a2a;
    --card-white: #ffffff;
    --card-fade: #eef0f2;
    --photo-top: #8f9aa3;
    --photo-bottom: #3b4046;
  }
  * { box-sizing: border-box; margin: 0; padding: 0; }
  html, body {
    width: 1200px; height: 871px; overflow: hidden;
    background: var(--page-bg);
    font-family: "Arimo", Arial, sans-serif;
  }
  .sheet {
    width: 1200px; height: 871px;
    display: flex; align-items: center; justify-content: center; gap: 40px;
  }
  .card {
    position: relative; width: 560px; height: 320px; overflow: hidden;
    box-shadow: 0 6px 18px rgba(0,0,0,.18);
  }

  /* Front */
  .card--front {
    background: linear-gradient(180deg, var(--card-white) 55%, var(--card-fade) 100%);
  }
  .brand {
    position: absolute; left: 40px; top: 38px; width: 250px;
    display: flex; align-items: center; gap: 10px;
    padding-bottom: 8px; border-bottom: 2px solid var(--brand-gold);
  }
  .brand__dot {
    width: 30px; height: 30px; border-radius: 50%; background: var(--brand-gold); flex: none;
  }
  .brand__name {
    font-size: 15px; font-weight: 700; color: var(--brand-blue); line-height: 18px;
  }
  .contact {
    position: absolute; left: 40px; top: 108px;
    font-size: 13px; line-height: 18px; color: var(--ink);
  }
  .contact__address { margin-bottom: 6px; }
  .contact__row { display: flex; align-items: center; gap: 8px; line-height: 20px; }
  .contact__icon { width: 13px; height: 13px; flex: none; }
  .rule-gold {
    position: absolute; left: 0; right: 0; top: 262px; height: 2px; background: var(--brand-gold);
  }
  .band-blue {
    position: absolute; left: 0; right: 0; top: 270px; bottom: 0;
    background: linear-gradient(90deg, var(--brand-blue-dark), var(--brand-blue));
  }
  .portrait {
    position: absolute; left: 392px; top: 52px; width: 128px; height: 150px;
    border-radius: 8px;
    background: linear-gradient(180deg, var(--photo-top), var(--photo-bottom));
    box-shadow: 0 2px 5px rgba(0,0,0,.3);
  }
  .person {
    position: absolute; left: 366px; width: 180px; top: 208px; text-align: center;
  }
  .person__name { font-size: 18px; font-weight: 700; color: var(--brand-blue); line-height: 20px; }
  .person__title { font-size: 14px; color: var(--brand-gold); line-height: 18px; margin-top: 2px; }

  /* Back */
  .card--back {
    background: radial-gradient(ellipse at 50% 40%, var(--brand-blue) 0%, var(--brand-blue-dark) 100%);
  }
  .back-brand {
    position: absolute; left: 0; right: 0; top: 118px;
    display: flex; align-items: center; justify-content: center; gap: 12px;
  }
  .back-brand__dot { width: 34px; height: 34px; border-radius: 50%; background: var(--brand-gold); flex: none; }
  .back-brand__name { font-size: 22px; font-weight: 700; color: var(--card-white); }
  .back-rule {
    position: absolute; left: 150px; width: 260px; top: 170px; height: 2px; background: var(--brand-gold);
  }
  .back-url {
    position: absolute; left: 0; right: 0; top: 186px; text-align: center;
    font-size: 12px; letter-spacing: 5px; color: var(--card-white);
  }
</style>
</head>
<body>
<main class="sheet">

  <section class="card card--front">
    <div class="brand">
      <span class="brand__dot"></span>
      <span class="brand__name">Plumwick Financial Services, Inc</span>
    </div>

    <div class="contact">
      <p class="contact__address">647 W Harlowe Street<br>Suite 312, Baltimore, MD 21201<br>NMLS #738516</p>
      <p class="contact__row">
        <svg class="contact__icon" viewBox="0 0 16 16" aria-hidden="true">
          <path fill="var(--brand-blue)" d="M3.5 1.5l2.5 0 1 3.5-1.6 1.2a8 8 0 0 0 4.4 4.4L11 9l3.5 1v2.5c0 1-1 2-2 2C6.5 14.5 1.5 9.5 1.5 3.5c0-1 1-2 2-2z"/>
        </svg>
        (800) 555-0142 x23
      </p>
      <p class="contact__row">
        <svg class="contact__icon" viewBox="0 0 16 16" aria-hidden="true">
          <rect x="4" y="1.5" width="8" height="5" fill="var(--brand-blue)"/>
          <rect x="1.5" y="6.5" width="13" height="6" rx="1" fill="var(--brand-blue)"/>
          <rect x="4" y="10" width="8" height="4.5" fill="var(--brand-blue)" stroke="#fff" stroke-width="1"/>
        </svg>
        (240) 555-0187
      </p>
      <p class="contact__row">
        <svg class="contact__icon" viewBox="0 0 16 16" aria-hidden="true">
          <circle cx="8" cy="8" r="7" fill="var(--brand-blue)"/>
          <path d="M1.5 8h13M8 1a10 10 0 0 1 0 14M8 1a10 10 0 0 0 0 14" stroke="#fff" stroke-width="1" fill="none"/>
        </svg>
        www.plumwickonline.com
      </p>
    </div>

    <div class="portrait" role="img" aria-label="Portrait photograph of the company president"></div>
    <div class="person">
      <p class="person__name">Marcus Hale</p>
      <p class="person__title">President</p>
    </div>

    <div class="rule-gold"></div>
    <div class="band-blue"></div>
  </section>

  <section class="card card--back">
    <div class="back-brand">
      <span class="back-brand__dot"></span>
      <span class="back-brand__name">Plumwick Financial Services</span>
    </div>
    <div class="back-rule"></div>
    <p class="back-url">plumwickonline.com</p>
  </section>

</main>
</body>
</html>
```